Business card design needed

see my website

www.calderwoodandpike.com

I am after a new logo and business card needs to fit in with the website. I like the look of typewriter text - would like this on the website as well if I could!

Industry/Entity Type

Business

Contact Information for Business Card

Calderwood and Pike
Design and Heritage Consultants

Marcia Dowell
Principal

+61 437 690 215
marcia@calderwoodandpike.com

www.calderwoodandpike.com

back of card

Interior Design
Consultancy on Period Home restoration and renovation
Heritage Impact Statements
Conservation Management Plans
Materials Conservation
Historical Research

```html
<!DOCTYPE html>
<html lang="en">
<head>
<meta charset="utf-8">
<title>Calderwood and Pike – Services</title>
<link rel="stylesheet" href="https://fonts.googleapis.com/css2?family=Special+Elite&display=swap">
<style>
  :root {
    --teal: #1f9d9b;
    --ink: #151515;
    --paper: #ffffff;
    --bar: #1a1414;
  }
  html, body {
    margin: 0;
    padding: 0;
    width: 1200px;
    height: 741px;
    overflow: hidden;
    background: var(--paper);
  }
  .card-back {
    position: relative;
    width: 1200px;
    height: 741px;
    background: var(--paper);
    font-family: "Special Elite", "Courier New", monospace;
    overflow: hidden;
  }
  .band-top {
    position: absolute;
    left: 0; top: 0;
    width: 1200px; height: 100px;
    background: var(--teal);
  }
  .band-bottom {
    position: absolute;
    left: 0; top: 726px;
    width: 1200px; height: 15px;
    background: var(--teal);
  }
  .band-accent {
    position: absolute;
    left: 103px; top: 726px;
    width: 303px; height: 15px;
    background: var(--bar);
  }
  .services {
    margin: 0;
    padding: 0;
    list-style: none;
  }
  .service {
    position: absolute;
    left: 0;
    width: 1200px;
    text-align: center;
    line-height: 1;
    white-space: nowrap;
    font-size: 40px;
  }
  .service--dark { color: var(--ink); }
  .service--teal { color: var(--teal); }
  .service--lead { top: 253px; }
  .service--wide { top: 303px; font-size: 34px; letter-spacing: 0.5px; }
  .service--impact { top: 354px; font-size: 41px; }
  .service--plans { top: 409px; }
  .service--materials { top: 463px; }
  .service--research { top: 517px; }
</style>
</head>
<body>
  <main class="card-back">
    <div class="band-top"></div>
    <ul class="services">
      <li class="service service--dark service--lead">Interior Design Consultancy</li>
      <li class="service service--teal service--wide">on Period Home restoration and renovation Heritage</li>
      <li class="service service--dark service--impact">Impact Statements</li>
      <li class="service service--teal service--plans">Conservation Management Plans</li>
      <li class="service service--dark service--materials">Materials Conservation</li>
      <li class="service service--teal service--research">Historical Research</li>
    </ul>
    <div class="band-bottom"></div>
    <div class="band-accent"></div>
  </main>
</body>
</html>
```